Business Card Design Project

We need a business card design for an existing company in Dallas/Fort Worth that is expanding services and re-branding. We are changing the name from Brightmoor Commercial Cleaning to Keystride Facility Services. We are expanding from only commercial cleaning to include complete commercial landscape and facility maintenance services, too.

As stated, we offer a package of services that includes landscape, janitorial and facility services, which is largely unique in the industry.

We would like a design that communicates trust/partnership with a professional, corporate image, but not necessarily using the standard white business card. We would like a design that perhaps uses darker blues or perhaps a gray background, but we are open to other ideas. We might also be interested in a double-sided design - maybe with our logo on the back, printed on a gray background?

We will probably stick with the attached logo, but if you've got another inspired idea....

Target Market(s)

Property managers, commercial real estate professionals, corporate executives

Industry/Entity Type

Landscape

Requirements
Should not have
• Not interested in old style fonts.

```html
<!DOCTYPE html>
<html lang="en">
<head>
<meta charset="utf-8">
<title>Keystride Facility Services – Business Card</title>
<link href="https://fonts.googleapis.com/css2?family=Questrial&display=swap" rel="stylesheet">
<style>
  :root {
    --backdrop: #dcd9d5;
    --card-gray: #a9a9a9;
    --card-white: #ffffff;
    --brand-navy: #1f4a6b;
    --chip: #e4e4e4;
    --text-gray: #6d6d6d;
    --rule-gray: #8f8f8f;
    --tab-gray: #a6a6a6;
  }
  * { margin: 0; padding: 0; box-sizing: border-box; }
  html, body {
    width: 1200px; height: 900px; overflow: hidden;
    background: var(--backdrop);
    font-family: "Questrial", "Century Gothic", sans-serif;
  }
  .stage { position: relative; width: 1200px; height: 900px; }

  .card { position: absolute; width: 578px; height: 322px; box-shadow: 0 4px 10px rgba(0,0,0,.25); }
  .card--back {
    left: 321px; top: 91px;
    background: radial-gradient(ellipse at 45% 40%, #b4b4b4 0%, var(--card-gray) 70%);
    border-radius: 0 36px 0 36px;
  }
  .card--front {
    left: 321px; top: 446px;
    background: var(--card-white);
    border-radius: 36px 0 36px 0;
  }

  .brand { display: flex; align-items: center; gap: 10px; }
  .brand__mark { background: var(--brand-navy); border-radius: 4px; flex: none; }
  .brand__name { color: var(--brand-navy); text-transform: uppercase; letter-spacing: .04em; white-space: nowrap; }

  .brand--chip {
    position: absolute; left: 142px; top: 112px; width: 315px; height: 67px;
    background: var(--chip); border-radius: 8px; padding: 0 10px 0 8px;
  }
  .brand--chip .brand__mark { width: 52px; height: 52px; }
  .brand--chip .brand__name { font-size: 22px; line-height: 1.1; }

  .brand--small { position: absolute; left: 52px; top: 89px; }
  .brand--small .brand__mark { width: 40px; height: 40px; }
  .brand--small .brand__name { font-size: 16px; line-height: 1.15; }

  .tab { position: absolute; left: 0; top: 82px; width: 15px; height: 58px; background: var(--tab-gray); }
  .divider { position: absolute; left: 290px; top: 67px; width: 2px; height: 200px; background: var(--rule-gray); }

  .contact { position: absolute; left: 316px; color: var(--text-gray); white-space: nowrap; }
  .contact__heading { top: 90px; font-size: 19px; letter-spacing: .02em; }
  .contact__person { top: 120px; font-size: 14.5px; line-height: 21px; }
  .contact__lines { top: 205px; font-size: 14px; line-height: 24px; }
</style>
</head>
<body>
<main class="stage">
  <section class="card card--back" aria-label="Card back">
    <div class="brand brand--chip">
      <span class="brand__mark"></span>
      <div class="brand__name">Keystride<br>Facility Services</div>
    </div>
  </section>

  <section class="card card--front" aria-label="Card front">
    <span class="tab"></span>
    <div class="brand brand--small">
      <span class="brand__mark"></span>
      <div class="brand__name">Keystride<br>Facility Services</div>
    </div>
    <span class="divider"></span>
    <div class="contact contact__heading">NAME SURNAME</div>
    <div class="contact contact__person">Mark Halloway<br>General Manager</div>
    <div class="contact contact__lines">www.keystridefacilityservices.com<br>000-000-0000</div>
  </section>
</main>
</body>
</html>
```